Tab-Fix Notes
3inx3in Tab Fix Notes with "Thank You!" message
Tab-Fix Notes - Corporate Services
Creative Brief
In need of designs for 3inch x 3inch Tab Fix Notes. Company Branding and Image (professional, high energy, uplifting, splash of color) The words "Thank You" and company website (www.marlowbrekke.com) must be included on actual tab fix.
Corporate Services
Corporate and professional, but modern.
3inch by 3 inch tab fix size. Use your creativity to the fullest but handwritten notes must legible on tab-fix. White backgrounds are okay as long as message stands out. Color preference of background - hot pink, orange, neon blue, neon green The words "Thank You" and company website (www.marlowbrekke.com) must be included on actual tab fix.
Related Contests
Social Media Banner Design (for Chatterloop, Zanvio+, Peepwire, and WorkNexa) based on current website.
Concepts
The Beacon Planning Institute Banner Display

```html
<!DOCTYPE html>
<html lang="en">
<head>
<meta charset="utf-8">
<title>Tab-Fix Notes – Thank You</title>
<link rel="stylesheet" href="https://fonts.googleapis.com/css2?family=Arimo:wght@400;700&family=Nothing+You+Could+Do&display=swap">
<style>
  :root {
    --board: #3a3939;
    --note-light: #eef86f;
    --note-mid: #d4eb55;
    --note-deep: #a5c93a;
    --brand-green: #17a83c;
    --brand-red: #a31e22;
    --ink-white: #ffffff;
  }
  html, body {
    margin: 0;
    padding: 0;
    width: 1200px;
    height: 795px;
    overflow: hidden;
    background: var(--board);
  }
  .note-card {
    display: block;
    width: 1200px;
    height: 795px;
  }
  .note-shape { fill: url(#noteGradient); }
  .site-address {
    font-family: "Arimo", Arial, sans-serif;
    font-weight: 700;
  }
  .site-address .site-prefix,
  .site-address .site-suffix {
    fill: var(--ink-white);
    font-size: 11px;
    font-weight: 400;
  }
  .site-address .site-name {
    fill: var(--brand-green);
    font-size: 19px;
    letter-spacing: 0.3px;
  }
  .brand-name {
    font-family: "Arimo", Arial, sans-serif;
    font-weight: 700;
    font-size: 8px;
    fill: var(--brand-red);
  }
  .thank-you {
    font-family: "Nothing You Could Do", cursive;
    font-size: 38px;
    fill: var(--ink-white);
  }
</style>
</head>
<body>
<svg class="note-card" viewBox="0 0 480 318" xmlns="http://www.w3.org/2000/svg">
  <defs>
    <linearGradient id="noteGradient" x1="0" y1="0" x2="1" y2="0.4">
      <stop offset="0" stop-color="var(--note-light)"/>
      <stop offset="0.55" stop-color="var(--note-mid)"/>
      <stop offset="1" stop-color="var(--note-deep)"/>
    </linearGradient>
    <path id="addressArc" d="M112 128 C130 60 270 35 335 110"/>
  </defs>

  <rect width="480" height="318" fill="var(--board)"/>

  <path class="note-shape"
        d="M100 132 C95 90 110 62 150 52 C200 40 270 38 310 60 C335 75 342 100 340 130
           C380 128 430 135 450 165 C465 190 455 235 430 245 C400 255 350 250 320 240
           C305 248 290 258 262 257 C250 250 245 248 230 247 L100 250
           C60 252 35 235 36 200 C36 165 60 140 100 132 Z"/>

  <text class="site-address">
    <textPath href="#addressArc" startOffset="2">
      <tspan class="site-prefix">www.</tspan><tspan class="site-name">marlowbrekke</tspan><tspan class="site-suffix">.com</tspan>
    </textPath>
  </text>

  <text class="brand-name" x="156" y="118" text-anchor="middle">Marlow Brekke</text>

  <text class="thank-you" x="235" y="205" text-anchor="middle">Thank You</text>
</svg>
</body>
</html>
```